Investor Slide Deck

Simple idea - take a model investor deck and build out a investor deck for K7R. I will complete the data, I need a template to work from within. I will attach a model investor deck and a blank K7R that I need built out to K7R. Use the K7R Pwrpt to build out the investor deck

```html
<!DOCTYPE html>
<html lang="en">
<head>
<meta charset="utf-8">
<title>K7R Investor Deck 2024</title>
<link href="https://fonts.googleapis.com/css2?family=Poppins:wght@400;500;600;700&display=swap" rel="stylesheet">
<style>
:root{
  --teal:#1d6e8b;
  --teal-deep:#1b6a86;
  --green:#14ae9f;
  --orange:#f15a22;
  --yellow:#f6c232;
  --ink:#333;
  --canvas:#e4e4e4;
  --white:#fff;
}
*{box-sizing:border-box;margin:0;padding:0}
html,body{width:1026px;height:1200px;overflow:hidden;background:var(--canvas);font-family:"Poppins",sans-serif;color:var(--ink)}
.deck{position:relative;width:1026px;height:1200px}
.slide{position:absolute;width:766px;height:430px;background:var(--white);overflow:hidden;transform:scale(.5793);transform-origin:0 0;box-shadow:0 10px 24px rgba(0,0,0,.12)}
.col-l{left:51px}.col-r{left:531px}
.row-1{top:54px}.row-2{top:335px}.row-3{top:616px}.row-4{top:897px}
.abs{position:absolute}
.header-band{position:absolute;left:0;top:0}
.slide-title{position:absolute;top:12px;left:44px;color:var(--white);font-size:26px;font-weight:400;white-space:nowrap}
.slide-title b{font-weight:700}
.brand{position:absolute;top:12px;right:44px;color:var(--orange);font-weight:600;font-size:34px;letter-spacing:1px;line-height:1}
.footer-line{position:absolute;left:0;top:413px;width:530px;height:1px;background:var(--orange)}
.footer-text{position:absolute;left:545px;top:405px;font-size:10px;color:#333}
.page-no{position:absolute;left:697px;top:401px;width:24px;height:24px;border-radius:50%;background:var(--yellow);color:var(--white);font-size:9px;font-weight:600;display:flex;align-items:center;justify-content:center}
.photo{position:absolute}
.h-small{font-size:11px;font-weight:600;color:var(--teal);text-transform:uppercase;line-height:1.3}
.body-small{font-size:7.5px;line-height:1.5;color:#333}
.center{text-align:center}
.icon-disc{position:absolute;border-radius:50%;display:flex;align-items:center;justify-content:center}
/* cover */
.cover-photo{left:0;top:0;width:766px;height:430px;background:linear-gradient(160deg,#8fb3cf 0%,#c9b58e 35%,#e3a35d 48%,#3f6f86 62%,#234f6a 100%)}
.cover-company{position:absolute;right:44px;top:282px;text-align:right;color:var(--teal);font-size:34px;line-height:1.1}
.cover-company b{font-weight:700;display:block}
.cover-sub{position:absolute;right:44px;top:372px;color:var(--orange);font-size:19px}
/* problems */
.lede{position:absolute;left:70px;top:78px;width:626px;text-align:center;font-size:11px;line-height:1.6;color:#222}
.prob-col{position:absolute;width:130px;top:128px;height:266px;border:1px dashed #bbb;border-radius:65px}
.prob-text{position:absolute;width:120px;text-align:center}
/* segments */
.seg-img{position:absolute;width:156px;height:123px}
.seg-card{position:absolute;width:140px;height:91px;background:var(--white);box-shadow:0 4px 10px rgba(0,0,0,.14);display:flex;align-items:center;justify-content:center;text-align:center;font-size:9px;font-weight:600;color:var(--teal);line-height:1.55;padding:0 8px}
/* products */
.prod-card{position:absolute;top:83px;width:204px;height:300px;background:var(--white);border-radius:20px;box-shadow:0 4px 12px rgba(0,0,0,.14);overflow:hidden}
.prod-card .img{height:140px}
.prod-card h3{font-size:10px;font-weight:600;color:var(--teal);margin:16px 14px 6px 15px;line-height:1.5}
.prod-card ul{list-style:none;margin:0 12px 0 15px}
.prod-card li{font-size:7.3px;line-height:1.45;position:relative;padding-left:11px;margin-bottom:4px}
.prod-card li::before{content:"";position:absolute;left:0;top:3px;width:3px;height:3px;border-radius:50%;background:var(--orange)}
.prod-card .bar{position:absolute;left:0;right:0;bottom:0;height:6px}
/* advantage */
.adv-item{position:absolute;width:310px}
.adv-item h3{font-size:11px;font-weight:600;color:var(--teal);margin-bottom:6px}
/* services */
.svc{position:absolute;width:200px}
.svc h3{font-size:11px;font-weight:600;color:var(--teal);margin-bottom:6px}
.svc.right-al{text-align:right}
/* thank you */
.thanks-bg{left:0;top:0;width:766px;height:430px;background:radial-gradient(ellipse at 25% 35%,#3a87a3 0%,#2a7a98 40%,#1f6e8d 100%)}
.thanks-title{position:absolute;left:44px;top:118px;color:var(--white);font-size:52px;font-weight:400;line-height:1}
.thanks-title b{font-weight:700}
.thanks-copy{position:absolute;left:44px;top:218px;width:310px;color:var(--white);font-size:11px;line-height:1.65;text-align:justify}
.contact{position:absolute;left:425px;display:flex;align-items:center;gap:20px;color:var(--white);font-size:13px;font-weight:500;line-height:1.4}
.contact .ring{width:35px;height:35px;border:1px solid rgba(255,255,255,.8);border-radius:50%;display:flex;align-items:center;justify-content:center;flex:none}
.contact .ring span{width:18px;height:18px;border-radius:50%;background:var(--yellow);display:flex;align-items:center;justify-content:center}
.follow{position:absolute;right:44px;top:393px;display:flex;align-items:center;gap:6px;color:var(--white);font-size:11px;font-weight:500}
.follow i{width:22px;height:22px;border-radius:50%;background:var(--white);display:block}
</style>
</head>
<body>
<main class="deck">

<!-- Cover -->
<section class="slide col-l row-1">
  <div class="photo cover-photo" role="img" aria-label="Photo of solar panels on a hillside with wind turbines at sunset"></div>
  <svg class="abs" style="left:0;top:0" width="766" height="430" viewBox="0 0 766 430">
    <path d="M390 430 C 470 360 470 240 580 205 C 660 178 730 200 766 225 L766 430 Z" fill="#fff"/>
    <rect x="350" y="305" width="160" height="52" rx="26" fill="#f6c232" opacity=".85" transform="rotate(-48 430 331)"/>
  </svg>
  <div class="brand" style="top:198px">K7R</div>
  <div class="cover-company"><b>Company</b>Name</div>
  <div class="cover-sub">Investor Deck, 2024</div>
</section>

<!-- Business Model -->
<section class="slide col-r row-1">
  <svg class="header-band" width="620" height="60" viewBox="0 0 620 60"><path d="M0 0H612C606 38 590 60 560 60H0Z" fill="#1d6e8b"/></svg>
  <h2 class="slide-title"><b>Business</b> Model</h2>
  <div class="brand">K7R</div>
  <div class="photo" style="left:64px;top:92px;width:638px;height:180px;border-radius:90px;background:linear-gradient(180deg,#9a8a5c 0%,#6d7a4c 30%,#5a6fa8 55%,#2d4d8c 100%)" role="img" aria-label="Photo of a large solar farm in autumn countryside"></div>
  <div class="icon-disc" style="left:198px;top:240px;width:64px;height:64px;background:var(--orange);border:4px solid #fff;box-shadow:0 3px 8px rgba(0,0,0,.2)">
    <svg width="28" height="28" viewBox="0 0 28 28" fill="none" stroke="#fff" stroke-width="2"><circle cx="14" cy="8" r="4"/><path d="M5 24l3-9h12l3 9z M10 15l-1 9 M18 15l1 9 M6 19h16"/></svg>
  </div>
  <div class="icon-disc" style="left:505px;top:240px;width:64px;height:64px;background:var(--green);border:4px solid #fff;box-shadow:0 3px 8px rgba(0,0,0,.2)">
    <svg width="28" height="28" viewBox="0 0 28 28" fill="none" stroke="#fff" stroke-width="2.4"><circle cx="14" cy="14" r="5"/><path d="M14 3v4M14 21v4M3 14h4M21 14h4M6 6l3 3M19 19l3 3M6 22l3-3M19 9l3-3"/></svg>
  </div>
  <div class="abs center" style="left:90px;top:318px;width:280px">
    <div class="h-small">Sales of Solar Panel</div>
    <p class="body-small" style="margin-top:6px">Solar Panels manufactured at our manufacturing facility will be sold via different channels that we will develop. We aim to reach out to B2C customers via a separate franchise model that we will begin after commencement of manufacturing operations.</p>
  </div>
  <div class="abs center" style="left:395px;top:318px;width:285px">
    <div class="h-small">Government and Industrial<br>EPC Projects</div>
    <p class="body-small" style="margin-top:6px">We project about half of our manufactured solar panels to be used in EPC projects that we will bid for. We aim to generate gross margins of 10% – 12% on the overall projects.</p>
  </div>
  <div class="footer-line"></div><div class="footer-text">Private &amp; Confidential | 2024</div><div class="page-no">05</div>
</section>

<!-- Problems -->
<section class="slide col-l row-2">
  <svg class="header-band" width="620" height="60" viewBox="0 0 620 60"><path d="M0 0H612C606 38 590 60 560 60H0Z" fill="#1d6e8b"/></svg>
  <h2 class="slide-title" style="left:38px"><b>Problems</b></h2>
  <div class="brand">K7R</div>
  <p class="lede">Every year, the rise in prices of electricity is burning a hole in the pocket of consumers. Solar Power is a reliable solution, but the industry is facing its own set of challenges.</p>

  <div class="prob-col" style="left:58px"></div>
  <div class="prob-col" style="left:188px"></div>
  <div class="prob-col" style="left:318px"></div>
  <div class="prob-col" style="left:448px"></div>
  <div class="prob-col" style="left:578px"></div>

  <div class="prob-text" style="left:63px;top:178px"><div class="h-small" style="font-size:9.5px">Poor Quality<br>Components</div><p class="body-small" style="margin-top:6px;font-size:7px">The use of low-quality solar panels and components in solar plant construction is impacting their efficiency and lifespan.</p></div>
  <div class="icon-disc" style="left:79px;top:279px;width:88px;height:88px;background:var(--orange)"><svg width="88" height="88"><circle cx="44" cy="44" r="35" fill="none" stroke="#fff" stroke-dasharray="4 3"/><circle cx="44" cy="40" r="10" fill="none" stroke="#fff" stroke-width="2.5"/><path d="M38 49l-4 12 10-4 10 4-4-12" fill="none" stroke="#fff" stroke-width="2.5"/></svg></div>

  <div class="icon-disc" style="left:209px;top:148px;width:88px;height:88px;background:var(--teal)"><svg width="88" height="88"><circle cx="44" cy="44" r="35" fill="none" stroke="#fff" stroke-dasharray="4 3"/><circle cx="44" cy="44" r="12" fill="none" stroke="#fff" stroke-width="3"/><path d="M38 44l4 4 8-8" fill="none" stroke="#fff" stroke-width="2.5"/></svg></div>
  <div class="prob-text" style="left:193px;top:250px"><div class="h-small" style="font-size:9.5px">Poor<br>Installation</div><p class="body-small" style="margin-top:6px;font-size:7px">Solar plant installations demand precision; poor installation can lead to downtime, damage, and efficiency loss.</p></div>

  <div class="prob-text" style="left:323px;top:165px"><div class="h-small" style="font-size:9.5px">Lack of<br>Awareness</div><p class="body-small" style="margin-top:6px;font-size:7px">Limited awareness of government subsidies and inadequate financing options for high-cost solar plant purchases can lead to missed product benefits</p></div>
  <div class="icon-disc" style="left:339px;top:279px;width:88px;height:88px;background:var(--yellow)"><svg width="88" height="88"><circle cx="44" cy="44" r="35" fill="none" stroke="#fff" stroke-dasharray="4 3"/><circle cx="44" cy="40" r="4" fill="#fff"/><path d="M37 58v-8a7 7 0 0 1 14 0v8z" fill="#fff"/><path d="M44 26v5M32 32l3 3M56 32l-3 3M28 44h5M60 44h-5" stroke="#fff" stroke-width="2"/></svg></div>

  <div class="icon-disc" style="left:469px;top:148px;width:88px;height:88px;background:var(--green)"><svg width="88" height="88"><circle cx="44" cy="44" r="35" fill="none" stroke="#fff" stroke-dasharray="4 3"/><path d="M44 28l13 5v9c0 9-6 15-13 18-7-3-13-9-13-18v-9z" fill="none" stroke="#fff" stroke-width="3"/><path d="M38 44l4 4 8-8" fill="none" stroke="#fff" stroke-width="2.5"/></svg></div>
  <div class="prob-text" style="left:453px;top:250px"><div class="h-small" style="font-size:9.5px">Unreliable<br>Customer and<br>Warranty Support</div><p class="body-small" style="margin-top:6px;font-size:7px">Challenges in reaching timely support and clarifying warranty terms can result in customer frustration and self-reliance for issue resolution.</p></div>

  <div class="prob-text" style="left:583px;top:150px"><div class="h-small" style="font-size:9.5px">Lack of<br>Transparency in<br>Pricing and<br>Performance</div><p class="body-small" style="margin-top:6px;font-size:7px">Customers might encounter unexpected hidden costs during installation and lower energy generation than initially agreed upon.</p></div>
  <div class="icon-disc" style="left:599px;top:279px;width:88px;height:88px;background:var(--orange)"><svg width="88" height="88"><circle cx="44" cy="44" r="35" fill="none" stroke="#fff" stroke-dasharray="4 3"/><circle cx="50" cy="37" r="9" fill="none" stroke="#fff" stroke-width="2.5"/><path d="M30 48h6v12h-6zM38 60h12l6-8-8-2-6-4" fill="none" stroke="#fff" stroke-width="2.5"/></svg></div>

  <div class="footer-line"></div><div class="footer-text">Private &amp; Confidential | 2024</div><div class="page-no">02</div>
</section>

<!-- Segments -->
<section class="slide col-r row-2">
  <svg class="header-band" width="620" height="60" viewBox="0 0 620 60"><path d="M0 0H612C606 38 590 60 560 60H0Z" fill="#1d6e8b"/></svg>
  <h2 class="slide-title" style="left:38px"><b>Our Business</b> Segments</h2>
  <div class="brand">K7R</div>
  <div class="seg-img" style="left:44px;top:120px;background:linear-gradient(180deg,#8aa0a8,#4f5d57 60%,#35425a)" role="img" aria-label="Photo of houses with rooftop solar panels"></div>
  <div class="seg-card" style="left:52px;top:227px;border-bottom:3px solid var(--orange)">GOVERNMENT<br>RESIDENTIAL HOUSE<br>OWNERS AND HOUSING<br>SOCIETIES</div>
  <div class="seg-img" style="left:219px;top:152px;background:linear-gradient(180deg,#a8c1d6,#7d94a8 50%,#6e5e58)" role="img" aria-label="Photo of a container port with cranes"></div>
  <div class="seg-card" style="left:227px;top:260px;border-bottom:3px solid var(--teal)">OEMS &amp; EXPORTS</div>
  <div class="seg-img" style="left:392px;top:120px;background:linear-gradient(180deg,#b7c9d8,#9ba5ad 45%,#3f5479)" role="img" aria-label="Photo of an industrial plant with solar panels"></div>
  <div class="seg-card" style="left:400px;top:227px;border-bottom:3px solid var(--yellow);align-items:flex-start;padding-top:16px">INDUSTRIES</div>
  <div class="seg-img" style="left:567px;top:152px;background:linear-gradient(180deg,#5d8fc4,#88a9cc 35%,#2e5f9c)" role="img" aria-label="Photo of a large utility-scale solar installation"></div>
  <div class="seg-card" style="left:575px;top:260px;border-bottom:3px solid var(--green)">GOVERNMENT<br>TENDERS AND UTILITY<br>PROJECTS</div>
  <div class="footer-line"></div><div class="footer-text">Private &amp; Confidential | 2024</div><div class="page-no">06</div>
</section>

<!-- Products -->
<section class="slide col-l row-3">
  <svg class="header-band" width="620" height="60" viewBox="0 0 620 60"><path d="M0 0H612C606 38 590 60 560 60H0Z" fill="#1d6e8b"/></svg>
  <h2 class="slide-title"><b>Our</b> Products</h2>
  <div class="brand">K7R</div>
  <article class="prod-card" style="left:58px">
    <div class="img" style="background:linear-gradient(180deg,#e0b36b,#6d7a45 55%,#c8ccd0)" role="img" aria-label="Photo of solar panels and blueprints on grass at sunset"></div>
    <h3>BI-FACIAL SOLAR PV<br>MODULE</h3>
    <ul><li>High Module Efficiency</li><li>Positive Power Tolerance upto 5 Watt</li><li>100% EL + VI Testing with 3 Stages</li><li>Increased Shade Tolerance</li><li>Split Junction Box Improves Heat Dissipation</li></ul>
    <div class="bar" style="background:var(--orange)"></div>
  </article>
  <article class="prod-card" style="left:281px">
    <div class="img" style="background:linear-gradient(180deg,#7fb0e0,#485a66 50%,#4e7a3a)" role="img" aria-label="Photo of grid tie inverter cabinets in a field"></div>
    <h3>SINGLE PHASE GRID TIE<br>INVERTERS</h3>
    <ul><li>High AC/DC Ratio for Higher Yields</li><li>Compact and Lightweight for easy installation.</li><li>User Friendly Web and App based monitoring.</li><li>Multiple MPPT Design With IDA Technology (Intelligent Disturbance Algorithm).</li></ul>
    <div class="bar" style="background:var(--green)"></div>
  </article>
  <article class="prod-card" style="left:505px">
    <div class="img" style="background:linear-gradient(180deg,#4f8fcf,#b6d1e6 50%,#365c9a 75%,#5d8a3c)" role="img" aria-label="Photo of solar panels with wind turbines under a blue sky"></div>
    <h3>THREE PHASE GRID TIE<br>INVERTERS</h3>
    <ul><li>Efficiency Upto 98.9%</li><li>Frequency Drop Control Technology</li><li>User Friendly Web and App based monitoring.</li><li>Weather, Consumption, String Level Monitoring System.</li></ul>
    <div class="bar" style="background:var(--yellow)"></div>
  </article>
  <div class="footer-line"></div><div class="footer-text">Private &amp; Confidential | 2024</div><div class="page-no">03</div>
</section>

<!-- Competitive Advantage -->
<section class="slide col-r row-3">
  <svg class="header-band" width="620" height="60" viewBox="0 0 620 60"><path d="M0 0H612C606 38 590 60 560 60H0Z" fill="#1d6e8b"/></svg>
  <h2 class="slide-title" style="left:38px"><b>Competitive</b> Advantage</h2>
  <div class="brand">K7R</div>
  <svg class="abs" style="left:0;top:0" width="766" height="430" viewBox="0 0 766 430">
    <path d="M270 135 A120 120 0 1 0 280 338" fill="none" stroke="#14ae9f" stroke-width="9"/>
    <path d="M290 92 C 350 140 400 200 340 350" fill="none" stroke="#aaa" stroke-width="1.5" stroke-dasharray="2 5"/>
    <circle cx="290" cy="92" r="2.5" fill="#999"/><circle cx="295" cy="338" r="2.5" fill="#999"/>
  </svg>
  <div class="photo" style="left:112px;top:108px;width:206px;height:206px;border-radius:50%;background:linear-gradient(180deg,#7fb0dd,#3a64a8 45%,#b7953e 80%,#6b6a3c)" role="img" aria-label="Photo of two engineers in safety vests inspecting solar panels"></div>
  <div class="icon-disc" style="left:327px;top:118px;width:52px;height:52px;background:var(--orange);border:3px solid #fff;box-shadow:0 3px 8px rgba(0,0,0,.2)"><svg width="26" height="26" fill="none" stroke="#fff" stroke-width="2.4"><circle cx="13" cy="13" r="9"/><path d="M9 13l3 3 5-6"/></svg></div>
  <div class="icon-disc" style="left:355px;top:214px;width:52px;height:52px;background:var(--teal);border:3px solid #fff;box-shadow:0 3px 8px rgba(0,0,0,.2)"><svg width="26" height="26" fill="none" stroke="#fff" stroke-width="2.4"><circle cx="13" cy="13" r="6"/><path d="M13 3v4M13 19v4M3 13h4M19 13h4"/></svg></div>
  <div class="icon-disc" style="left:327px;top:297px;width:52px;height:52px;background:var(--yellow);border:3px solid #fff;box-shadow:0 3px 8px rgba(0,0,0,.2)"><svg width="26" height="26" fill="#fff"><circle cx="9" cy="8" r="3"/><path d="M4 21v-6a5 5 0 0 1 10 0v6z"/><circle cx="19" cy="11" r="2.5"/><path d="M15 21v-4a4 4 0 0 1 8 0v4z"/></svg></div>
  <div class="adv-item" style="left:404px;top:122px"><h3>FOCUS ON QUALITY</h3><p class="body-small">Our stringent quality control methods enable us to provide high-quality products that we provide warranties upto 25 years.</p></div>
  <div class="adv-item" style="left:432px;top:218px"><h3>STATE OF THE ART TECHNOLOGY</h3><p class="body-small">Our access to advanced technology lets us create cutting-edge solar solutions that adapt flexibly to suit specific requirements.</p></div>
  <div class="adv-item" style="left:404px;top:308px"><h3>UNRIVALLED EXPERIENCE</h3><p class="body-small">We have worked on 2500+ projects with a diverse client base while maintaining consistent quality. Experience and Technology enable us to provide best results for our customers.</p></div>
  <div class="footer-line"></div><div class="footer-text">Private &amp; Confidential | 2024</div><div class="page-no">07</div>
</section>

<!-- Services -->
<section class="slide col-l row-4">
  <svg class="header-band" width="620" height="60" viewBox="0 0 620 60"><path d="M0 0H612C606 38 590 60 560 60H0Z" fill="#1d6e8b"/></svg>
  <h2 class="slide-title"><b>Our</b> Services</h2>
  <div class="brand">K7R</div>
  <svg class="abs" style="left:276px;top:124px" width="214" height="216" viewBox="0 0 214 216">
    <path d="M8 8H60A40 40 0 0 1 100 48V100H48A40 40 0 0 1 8 60Z" fill="none" stroke="#f15a22" stroke-width="7"/>
    <path d="M206 8H154A40 40 0 0 0 114 48V100H166A40 40 0 0 0 206 60Z" fill="none" stroke="#1d6e8b" stroke-width="7"/>
    <path d="M8 208H60A40 40 0 0 0 100 168V116H48A40 40 0 0 0 8 156Z" fill="none" stroke="#14ae9f" stroke-width="7"/>
    <path d="M206 208H154A40 40 0 0 1 114 168V116H166A40 40 0 0 1 206 156Z" fill="none" stroke="#f6c232" stroke-width="7"/>
    <g fill="none" stroke="#f15a22" stroke-width="2.5"><circle cx="54" cy="44" r="8"/><path d="M50 56h8M40 72h10l8-6M40 64v12"/></g>
    <g fill="none" stroke="#1d6e8b" stroke-width="3"><path d="M146 40l24 24M170 40l-24 24"/><circle cx="144" cy="38" r="4"/></g>
    <g fill="none" stroke="#14ae9f" stroke-width="2.5"><path d="M36 172l14-14h20l-14 14z"/><circle cx="66" cy="150" r="6"/><path d="M66 138v-4M76 150h4M74 142l3-3"/></g>
    <g fill="none" stroke="#f6c232" stroke-width="3"><circle cx="160" cy="162" r="9"/><path d="M160 146v5M160 173v5M144 162h5M171 162h5M149 151l3 3M168 170l3 3M149 173l3-3M168 154l3-3"/></g>
  </svg>
  <div class="svc right-al" style="left:58px;top:130px"><h3>EPC SOLUTIONS</h3><p class="body-small">Get turnkey EPC solutions that cover engineering, procurement, and construction. We develop long-term solutions that have a direct impact on the environment. Take care of all your electricity requirements.</p></div>
  <div class="svc right-al" style="left:58px;top:255px"><h3>SOLAR FINANCING</h3><p class="body-small">With our assistance, you can finance the installation of solar panels and renewable energy. We locate the best source for you to apply for and obtain the best solar loans.</p></div>
  <div class="svc" style="left:506px;top:130px;width:210px"><h3>INSTALLATION AND COMMISSION</h3><p class="body-small">With our 24/7 remote monitoring, you may install and run solar panels without worrying about performance issues. We offer complete solutions. We provide support for all the systems we install for you.</p></div>
  <div class="svc" style="left:506px;top:255px"><h3>OPERATION AND MAINTENANCE</h3><p class="body-small">Get expert advice on how to run the solar plant once it has been installed. To care for your system and maintain its proper operation, we adhere to all applicable rules.</p></div>
  <div class="footer-line"></div><div class="footer-text">Private &amp; Confidential | 2024</div><div class="page-no">04</div>
</section>

<!-- Thank You -->
<section class="slide col-r row-4">
  <div class="photo thanks-bg" role="img" aria-label="Faint teal-tinted photo of a worker installing solar panels"></div>
  <div class="brand" style="color:var(--white)">K7R</div>
  <h2 class="thanks-title"><b>Thank</b> You</h2>
  <svg class="abs" style="left:0;top:188px" width="120" height="14"><path d="M0 7H104" stroke="#f15a22" stroke-width="2"/><circle cx="104" cy="7" r="6" fill="#f15a22"/></svg>
  <p class="thanks-copy">Every year, the rise in prices of electricity is burning a hole in the pocket of consumers. Solar Power is a reliable solution, but the industry is facing its own set of challenges.</p>
  <div class="abs" style="left:392px;top:85px;width:2px;height:258px;background:var(--white)"></div>
  <div class="contact" style="top:120px"><div class="ring"><span><svg width="10" height="10" viewBox="0 0 10 10"><path d="M2 1l2 2-1 1a5 5 0 0 0 3 3l1-1 2 2-1 1C4 9 1 6 1 2z" fill="#fff"/></svg></span></div>+1 (555) 014 2290</div>
  <div class="contact" style="top:170px"><div class="ring"><span><svg width="10" height="8"><rect x=".5" y=".5" width="9" height="7" fill="none" stroke="#fff"/><path d="M.5 .5L5 4l4.5-3.5" fill="none" stroke="#fff"/></svg></span></div>info@k7rsolar.com</div>
  <div class="contact" style="top:220px"><div class="ring"><span><svg width="10" height="10"><circle cx="5" cy="5" r="4" fill="none" stroke="#fff"/><path d="M1 5h8M5 1v8" stroke="#fff" stroke-width=".8"/></svg></span></div>www.k7rsolar.com</div>
  <div class="contact" style="top:268px"><div class="ring"><span><svg width="8" height="11" viewBox="0 0 8 11"><path d="M4 11C1 7 0 5 0 4a4 4 0 0 1 8 0c0 1-1 3-4 7z" fill="#fff"/></svg></span></div>218 Harbor Field Road,<br>United States</div>
  <div class="follow">Follow Us On <i></i><i></i></div>
</section>

</main>
</body>
</html>
```